The Duchess of Nestwares is an online store specialising in all things for the home Bathroom, Kitchen,

I need a business card designed that is professional and elegant, yet not conservative. We will be wanting to brand the entire business and will have videos made where we will be interacting with the product, testing the products and basically creating an online interactive community for all those people interested in all things to do with the Home and the activities that take place in and around the home.

Target Market(s)

30-65yr old Men and Women who LOVE their Home and see it as their primary place of Happiness, their sanctuary!

Industry/Entity Type

Business

Contact Information for Business Card

www.duchessofnestwares.example The Duchess Of Nestwares-PO Box 58391, Mt Ferndale, Auckland. NEW ZEALAND. info@duchessofnestwares.example
Love your Home! Lorraine Becker-Duponte

Font styles to use
Decorative
Script

Colors
9bcb3b
33b8a4
85cae6
b7a5cd
eda3c7
e667a6
d2a4cc
fdf9cf
fee18a

Requirements
Must have
• Attractive colours. Must feel Elegant, yet simple. A font that is rounded without sharp edges. Organic feel to the card, something raw with texture.
Nice to have
• I like the logo deign that I gave in the photos, something feminine, but fun.
Should not have
• I dont like sharp edges, or linear design. I like organic, flowing, fractal type design. Something that looks beautiful in form when you look at it.

```html
<!DOCTYPE html>
<html lang="en">
<head>
<meta charset="utf-8">
<title>The Duchess of Nestwares — Business Card</title>
<link rel="stylesheet" href="https://fonts.googleapis.com/css2?family=Questrial&display=swap">
<style>
  :root {
    --stage: #2b2b2b;
    --brand-blue: #459ec8;
    --brand-pink: #e5298a;
    --card-white: #ffffff;
    --ink-white: #ffffff;
  }
  * { margin: 0; padding: 0; box-sizing: border-box; }
  html, body { width: 1189px; height: 1200px; overflow: hidden; }
  body {
    background: var(--stage);
    font-family: "Questrial", "Helvetica Neue", Arial, sans-serif;
    position: relative;
  }
  .card {
    position: absolute;
    left: 170px;
    width: 857px;
    height: 490px;
    border-radius: 30px;
  }
  .card--front { top: 66px; background: var(--brand-blue); }
  .card--back  { top: 625px; background: var(--card-white); }

  /* Front */
  .front-name {
    position: absolute;
    left: 0; right: 0; top: 232px;
    text-align: center;
    color: var(--ink-white);
    font-size: 40px;
    font-weight: 400;
    line-height: 1.2;
    white-space: nowrap;
  }
  .social-row {
    position: absolute;
    left: 0; right: 0; top: 399px;
    display: flex;
    justify-content: center;
    gap: 12px;
  }
  .social-dot {
    width: 34px; height: 34px;
    border: 2px solid var(--ink-white);
    border-radius: 50%;
  }

  /* Back */
  .back-name {
    position: absolute;
    left: 50px; width: 350px; top: 226px;
    text-align: center;
    color: var(--brand-blue);
    font-size: 27px;
    font-weight: 400;
    line-height: 1.2;
    white-space: nowrap;
  }
  .divider {
    position: absolute;
    left: 420px; top: 162px;
    width: 1.5px; height: 161px;
    background: var(--brand-pink);
  }
  .person {
    position: absolute;
    left: 465px; top: 158px;
  }
  .person__name { color: var(--brand-blue); font-size: 26px; line-height: 1.05; }
  .person__surname { color: var(--brand-pink); font-size: 20px; line-height: 1.1; }
  .contact-list {
    position: absolute;
    left: 463px; top: 245px;
    list-style: none;
  }
  .contact-list li {
    display: flex;
    align-items: center;
    gap: 9px;
    height: 28px;
    color: var(--brand-blue);
    font-size: 21px;
    white-space: nowrap;
  }
  .contact-list svg { width: 24px; height: 24px; flex: none; }
  .address {
    position: absolute;
    left: 0; right: 0; top: 406px;
    text-align: center;
    color: var(--brand-blue);
    font-size: 19px;
  }
</style>
</head>
<body>
  <section class="card card--front" aria-label="Card front">
    <h1 class="front-name">The Duchess of Nestwares</h1>
    <div class="social-row" aria-label="Social profiles">
      <span class="social-dot"></span>
      <span class="social-dot"></span>
      <span class="social-dot"></span>
      <span class="social-dot"></span>
      <span class="social-dot"></span>
      <span class="social-dot"></span>
    </div>
  </section>

  <section class="card card--back" aria-label="Card back">
    <h2 class="back-name">The Duchess of Nestwares</h2>
    <div class="divider"></div>
    <div class="person">
      <p class="person__name">Lorraine Becker</p>
      <p class="person__surname">Duponte</p>
    </div>
    <ul class="contact-list">
      <li>
        <svg viewBox="0 0 24 24" aria-hidden="true"><circle cx="12" cy="12" r="11" fill="none" stroke="#e5298a" stroke-width="1.6"/><path d="M7 10c0-2 10-2 10 0v1h-2.5v-1.2h-5V11H7z M8.5 12h7l1 5h-9z" fill="#e5298a"/></svg>
        <span>64-210553172</span>
      </li>
      <li>
        <svg viewBox="0 0 24 24" aria-hidden="true"><circle cx="12" cy="12" r="11" fill="none" stroke="#e5298a" stroke-width="1.6"/><rect x="6.5" y="8" width="11" height="8" fill="#e5298a"/><path d="M6.5 8l5.5 4.5L17.5 8M6.5 16l4-4M17.5 16l-4-4" stroke="#fff" stroke-width="1" fill="none"/></svg>
        <span>info@duchessofnestwares.example</span>
      </li>
      <li>
        <svg viewBox="0 0 24 24" aria-hidden="true"><circle cx="12" cy="12" r="11" fill="none" stroke="#e5298a" stroke-width="1.6"/><circle cx="12" cy="12" r="6" fill="none" stroke="#e5298a" stroke-width="1.3"/><path d="M6 12h12M12 6v12M8 8.5h8M8 15.5h8" stroke="#e5298a" stroke-width="1"/><ellipse cx="12" cy="12" rx="2.8" ry="6" fill="none" stroke="#e5298a" stroke-width="1"/></svg>
        <span>www.duchessofnestwares.example</span>
      </li>
    </ul>
    <p class="address">PO Box 58391, Mt Ferndale, Auckland. NEW ZEALAND.</p>
  </section>
</body>
</html>
```